Postcard Design January 2015

I need a postcard designed to introduce my company to potential new customers in the UK. My company is QT Page Solutions based in Chester and we represent one of Poland's leading and long established book printers. We offer competitive pricing, consistently high levels of print and binding quality and industry leading levels of customer service. We have been meeting the print requirements of UK publishers for more than 10 years.

```html
<!DOCTYPE html>
<html lang="en">
<head>
<meta charset="utf-8">
<title>QT Page Solutions – Postcard</title>
<link rel="stylesheet" href="https://fonts.googleapis.com/css2?family=Oswald:wght@400;500;700&display=swap">
<style>
  :root {
    --yellow: #f4e52c;
    --ink: #4a1b1f;
    --paper: #ffffff;
    --mist: #ecebe8;
    --backdrop: #e9e6e1;
    --photo-light: #efe9e2;
    --photo-mid: #a89583;
    --photo-dark: #6f5a4d;
    --pages-light: #e7e3da;
    --pages-dark: #b9b3a6;
  }
  * { box-sizing: border-box; margin: 0; padding: 0; }
  html, body { width: 1200px; height: 800px; overflow: hidden; }
  body {
    background: var(--backdrop);
    font-family: "Oswald", "Arial Narrow", sans-serif;
    color: var(--ink);
    position: relative;
  }
  .card {
    position: absolute;
    top: 198px;
    width: 570px;
    height: 404px;
    background: var(--paper);
    overflow: hidden;
    box-shadow: 0 6px 18px rgba(0,0,0,0.18);
  }
  .card--back { left: 20px; }
  .card--front { left: 610px; }
  .card svg.shapes { position: absolute; inset: 0; }

  /* Back side */
  .benefits {
    position: absolute; left: 38px; top: 52px;
    list-style: none;
    font-weight: 700; font-size: 21px; line-height: 1.22;
    text-transform: uppercase;
  }
  .benefits li::before { content: "» "; }
  .details {
    position: absolute; left: 48px; top: 212px; width: 480px;
    list-style: none;
    font-weight: 400; font-size: 12.5px; line-height: 1.5;
  }
  .details li { margin-bottom: 6px; padding-left: 10px; position: relative; }
  .details li::before { content: "•"; position: absolute; left: 0; }

  /* Front side */
  .brand {
    position: absolute; left: 34px; top: 22px;
    font-weight: 700; font-size: 44px; line-height: 1;
    text-transform: uppercase;
  }
  .services {
    position: absolute; left: 34px; top: 74px;
    font-weight: 700; font-size: 15px; letter-spacing: 0.2px;
    text-transform: uppercase;
  }
  .slogan {
    position: absolute; right: 26px; top: 300px;
    font-weight: 700; font-size: 34px; line-height: 1;
  }
  .contact {
    position: absolute; right: 26px; top: 344px; text-align: left;
    width: 318px;
  }
  .contact__phone { font-weight: 700; font-size: 17px; text-transform: uppercase; }
  .contact__web { font-weight: 400; font-size: 11.5px; margin-top: 2px; }
</style>
</head>
<body>

<section class="card card--back" aria-label="Postcard back">
  <svg class="shapes" width="570" height="404" viewBox="0 0 570 404">
    <defs>
      <linearGradient id="pages" x1="0" y1="0" x2="1" y2="0">
        <stop offset="0" stop-color="var(--pages-light)"/>
        <stop offset="0.5" stop-color="var(--pages-dark)"/>
        <stop offset="1" stop-color="var(--pages-light)"/>
      </linearGradient>
    </defs>
    <polygon points="0,0 570,0 570,105 0,190" fill="var(--mist)"/>
    <polygon points="0,0 570,0 570,85 0,172" fill="var(--yellow)"/>
    <rect x="0" y="318" width="570" height="86" fill="url(#pages)" role="img" aria-label="Photo of stacked book page edges"/>
  </svg>
  <ul class="benefits">
    <li>High quality book printing and binding</li>
    <li>Competitive pricing</li>
    <li>Excellent customer service</li>
  </ul>
  <ul class="details">
    <li>We produce paperback and hardback books in mono or colour. Binding options include sewn, perfect, Wiro-o and saddle stitched.</li>
    <li>Print finishing includes lamination, spot UV and foil blocking.</li>
    <li>We have state of the art production equipment, use quality materials and follow strict quality control procedures.</li>
    <li>We have weekly shipments in to the UK.</li>
  </ul>
</section>

<section class="card card--front" aria-label="Postcard front">
  <svg class="shapes" width="570" height="404" viewBox="0 0 570 404">
    <defs>
      <linearGradient id="type-photo" x1="0" y1="0" x2="1" y2="1">
        <stop offset="0" stop-color="var(--photo-dark)"/>
        <stop offset="0.45" stop-color="var(--photo-mid)"/>
        <stop offset="1" stop-color="var(--photo-light)"/>
      </linearGradient>
    </defs>
    <rect x="0" y="0" width="570" height="404" fill="url(#type-photo)" role="img" aria-label="Photo of metal letterpress blocks spelling PRINT"/>
    <polygon points="0,110 570,40 570,150 0,175" fill="var(--paper)" opacity="0.35"/>
    <polygon points="0,0 570,0 570,50 470,130 0,130" fill="var(--yellow)"/>
    <polygon points="120,404 230,270 570,270 570,404" fill="var(--paper)" opacity="0.35"/>
    <polygon points="170,404 250,285 570,285 570,404" fill="var(--yellow)"/>
  </svg>
  <h1 class="brand">QT Page Solutions</h1>
  <p class="services">Litho &amp; digital printing, bookbinding &amp; finishing</p>
  <p class="slogan">book printing made easy</p>
  <div class="contact">
    <p class="contact__phone">Call us: 01632 960481 • 07700 900312</p>
    <p class="contact__web">www.qtpagesolutions.co.uk • sam.harlow@qtpagesolutions.co.uk</p>
  </div>
</section>

</body>
</html>
```